Design a clean homepage for a travel portal based in the US catering to Asians. The design should be able to be used on other pages, or color scheme menu layout, header and footer should be usable on other pages.

Include the main options for users to click, as an example some could be; 1. Local Tour Company 2. Local Tour Guide 3. Transportation Company 4. Tour Packages

Think like www.makerlinkhub.net who brings designers and clients together we are bringing Tour company, Tour guide, Bus/Transportation company directly to those who need it. This is for a two way portal, not a common one way portal like regular booking sites.

Assume that a person arrives or is planning on arriving at a destination, what are some options that should be on the page, layout of the options: squares, rectangles, stars, scroll slides, whatever makes you feel fun, elegant, fresh, uplifting.

Feelings we want to convey: fun, elegant, fresh, uplifting, interesting, energetic

Update:
When we said this should be a simple design, we meant simple for the end user to understand what was going on. I have attached a screenshot of a website, that it is very easy to understand what its purpose is.

How you decide to set up picture/scenery areas, logo area, menu area, where the options go is all up to you. Would like it to be clean and inviting, we would also like the options to be colors that call the users to action(make them click). This doesn't have to be colors so much as design. If you have further questions feel free to message me.

Attached is our logo in various styles for you to choose from.

Target Market(s)

Travel, package tours, international students, business trips

Industry/Entity Type

Travel Industry

Number of Pages Required

1 page

Colors
ec1f27
ffffff
0255a3
474747
7f7f7f
5c5c5c
aaaaaa

Requirements
Must have
• 1. Local Tour Company 2. Local Tour Guide 3. Transportation Company 4. Tour Packages
Should not have
• Our main goal is not to sell flights or hotel rooms, so this can be an element on the page(or not) but it should not be very central/obvious.

```html
<!DOCTYPE html>
<html lang="en">
<head>
<meta charset="utf-8">
<title>Travel Portal – Home</title>
<link rel="stylesheet" href="https://fonts.googleapis.com/css2?family=Pacifico&family=Source+Sans+3:wght@400;600&display=swap">
<style>
:root{
  --red:#e0141e;
  --deep-red:#c20008;
  --script-red:#c8000a;
  --blue:#0255a3;
  --text-grey:#7f7f7f;
  --dark:#2a2a2a;
  --white:#ffffff;
  --rule:#b9bcbf;
}
*{box-sizing:border-box;margin:0;padding:0}
html,body{width:1141px;height:1200px;overflow:hidden}
body{position:relative;font-family:"Source Sans 3",Arial,sans-serif;background:var(--white)}

.site-header{position:absolute;left:0;top:0;width:1141px;height:73px;background:var(--white)}
.main-nav a{position:absolute;top:33px;font-size:20px;color:var(--red);text-decoration:none;letter-spacing:.3px}
.account-link{position:absolute;right:175px;top:13px;font-size:8px;color:#8a8a8a}
.search-box{position:absolute;left:830px;top:38px;width:137px;height:22px;border:1px solid var(--red);border-radius:5px;background:var(--white)}
.search-box span{position:absolute;left:10px;top:5px;font-size:8px;color:var(--red)}
.search-box svg{position:absolute;right:7px;top:3px}

.page-backdrop{position:absolute;left:0;top:73px;width:1141px;height:1046px;
  background:linear-gradient(180deg,#2f73bc 0%,#4a8fd0 12%,#7fb3e0 22%,#4e99d4 33%,#2585c5 35%,#2d9bd2 42%,#49b4da 52%,#8fcfdf 58%,#dceff2 63%,#f1f3f1 70%,#eae6df 76%,#ececeb 84%,#eeeeee 100%)}

.polaroid{position:absolute;background:var(--white);box-shadow:2px 3px 6px rgba(0,0,0,.35)}
.polaroid .photo{position:absolute}
.hero-back-left{left:178px;top:170px;width:390px;height:305px;transform:rotate(-1.5deg)}
.hero-back-left .photo{left:20px;top:16px;width:330px;height:220px;background:linear-gradient(135deg,#4a8fd8,#2d6fb8 50%,#334a6a)}
.hero-back-mid{left:290px;top:110px;width:390px;height:300px;transform:rotate(5deg)}
.hero-back-mid .photo{left:22px;top:18px;width:340px;height:225px;background:linear-gradient(135deg,#6b8a4e,#b49070 45%,#d9cfae)}
.hero-back-right{left:660px;top:138px;width:292px;height:300px;transform:rotate(-3deg)}
.hero-back-right .photo{left:60px;top:16px;width:212px;height:222px;background:linear-gradient(160deg,#c9cfa9,#a79a78 50%,#3a3733)}
.hero-front{left:405px;top:140px;width:385px;height:318px;transform:rotate(4deg)}
.hero-front .photo{left:20px;top:18px;width:345px;height:225px;background:linear-gradient(160deg,#8ec6e8,#b8d6e6 40%,#7d8c90 75%,#4b5a62)}
.hero-front .caption{position:absolute;left:0;right:0;top:258px;text-align:center;font-family:"Pacifico",cursive;font-size:15px;color:var(--script-red)}

.slider-arrow{position:absolute;top:287px}
.slider-arrow.prev{left:104px}
.slider-arrow.next{left:1026px}

.tagline{position:absolute;left:173px;width:794px;top:530px;text-align:center;font-family:"Pacifico",cursive;font-size:49px;color:var(--script-red);letter-spacing:-1px;white-space:nowrap}
.divider{position:absolute;left:173px;width:794px;height:1px;background:var(--rule)}

.service-card{position:absolute;width:161px;height:131px;background:var(--white);box-shadow:2px 3px 5px rgba(0,0,0,.3);text-decoration:none}
.service-card .photo{position:absolute;left:8px;top:7px;width:145px;height:97px;background:linear-gradient(165deg,#1d3a5c,#3b5f80 45%,#3f5c3a 80%,#22331f);display:flex;align-items:center;justify-content:center;text-align:center}
.service-card .title{font-family:"Pacifico",cursive;font-size:20px;line-height:26px;color:var(--white)}
.service-card .more{position:absolute;left:0;right:0;bottom:7px;text-align:center;font-size:9.5px;color:var(--dark)}

.welcome-title{position:absolute;left:173px;top:852px;font-family:"Pacifico",cursive;font-size:43px;color:var(--blue);letter-spacing:-1px}
.welcome-photo{position:absolute;left:173px;top:938px;width:123px;height:123px;background:linear-gradient(180deg,#3d86c6,#2a6fae 45%,#3b6b3c 75%,#22481f)}
.welcome-copy{position:absolute;left:308px;top:937px;width:662px;font-size:7.7px;line-height:9.9px;color:var(--text-grey)}
.welcome-copy p{margin-bottom:10px}
.read-more{position:absolute;left:308px;top:1052px;font-size:9px;color:#5c5c5c}

.site-footer{position:absolute;left:0;top:1119px;width:1141px;height:81px;background:var(--deep-red)}
.to-top{position:absolute;left:1034px;top:22px}
</style>
</head>
<body>
<header class="site-header">
  <nav class="main-nav">
    <a href="#" style="left:172px">Home</a>
    <a href="#" style="left:246px">About us</a>
    <a href="#" style="left:345px">Lorem</a>
    <a href="#" style="left:416px">Ipsum</a>
    <a href="#" style="left:492px">Contact us</a>
  </nav>
  <div class="account-link">Sign in / Register</div>
  <div class="search-box"><span>search</span>
    <svg width="15" height="15" viewBox="0 0 15 15"><circle cx="6" cy="6" r="4.6" fill="none" stroke="#e0141e" stroke-width="1.3"/><line x1="9.4" y1="9.4" x2="14" y2="14" stroke="#e0141e" stroke-width="1.5"/></svg>
  </div>
</header>

<main>
  <div class="page-backdrop" role="img" aria-label="Blue sky with clouds over a turquoise sea and a sandy beach"></div>

  <section class="hero-slider">
    <div class="polaroid hero-back-left"><div class="photo" role="img" aria-label="Backpacker at a harbour with sailboats"></div></div>
    <div class="polaroid hero-back-mid"><div class="photo" role="img" aria-label="Traveller reading a map outdoors"></div></div>
    <div class="polaroid hero-back-right"><div class="photo" role="img" aria-label="World map and old book with a travel note"></div></div>
    <div class="polaroid hero-front">
      <div class="photo" role="img" aria-label="Smiling travel couple in front of famous European landmarks"></div>
      <div class="caption">Duis autem vel eum iriure dolor in hendrerit</div>
    </div>
    <svg class="slider-arrow prev" width="16" height="28" viewBox="0 0 16 28"><polyline points="13,3 3,14 13,25" fill="none" stroke="#fff" stroke-width="3"/></svg>
    <svg class="slider-arrow next" width="16" height="28" viewBox="0 0 16 28"><polyline points="3,3 13,14 3,25" fill="none" stroke="#fff" stroke-width="3"/></svg>
  </section>

  <h1 class="tagline">Creating memories that lasts forever!</h1>
  <div class="divider" style="top:622px"></div>

  <section class="services">
    <a class="service-card" href="#" style="left:175px;top:657px;transform:rotate(-3deg)">
      <div class="photo" role="img" aria-label="Harbour city with mountain at dusk"><span class="title">Local Tour<br>Company</span></div>
      <span class="more">find out more &gt;&gt;</span></a>
    <a class="service-card" href="#" style="left:386px;top:670px;transform:rotate(8deg)">
      <div class="photo" role="img" aria-label="Harbour city with mountain at dusk"><span class="title">Local Tour<br>Guide</span></div>
      <span class="more">find out more &gt;&gt;</span></a>
    <a class="service-card" href="#" style="left:577px;top:677px">
      <div class="photo" role="img" aria-label="Harbour city with mountain at dusk"><span class="title">Transportation<br>Company</span></div>
      <span class="more">find out more &gt;&gt;</span></a>
    <a class="service-card" href="#" style="left:783px;top:667px;transform:rotate(3deg)">
      <div class="photo" role="img" aria-label="Harbour city with mountain at dusk"><span class="title">Tour<br>Packages</span></div>
      <span class="more">find out more &gt;&gt;</span></a>
  </section>

  <div class="divider" style="top:840px"></div>

  <section class="welcome">
    <h2 class="welcome-title">Welcome to our site!</h2>
    <div class="welcome-photo" role="img" aria-label="Hilltop statue overlooking a bay city"></div>
    <div class="welcome-copy">
      <p>Duis autem vel eum iriure dolor in hendrerit in vulputate velit esse molestie consequat, vel illum dolore eu feugiat nulla facilisis at vero eros et accumsan et iusto odio dignissim qui blandi. Duis autem vel eum iriure dolor in hendrerit in vulputate velit esse molestie consequat, vel illum dolore eu feugiat nulla facilisis at vero eros et accumsan et iusto odio dignissim qui blandi Duis autem vel eum iriure dolor in hendrerit in vulputate velit esse molestie consequat, vel illum dolore eu feugiat nulla facilisis at vero eros et accumsan et iusto odio dignissim qui blandi.</p>
      <p>Duis autem vel eum iriure dolor in hendrerit in vulputate velit esse molestie consequat, vel illum dolore eu feugiat nulla facilisis at vero eros et accumsan et iusto odio dignissim qui blandi. Duis autem vel eum iriure dolor in hendrerit in vulputate velit esse molestie consequat, vel illum dolore eu feugiat nulla facilisis at vero Duis autem vel eum iriure dolor in hendrerit in vulputate velit esse molestie consequat, vel illum dolore eu feugiat nulla facilisis at vero eros et accumsan et iusto odio dignissim qui blandi. Duis autem vel eum iriure dolor in hendrerit in vulputate velit esse molestie consequat, vel illum dolore eu feugiat nulla facilisis at vero eros et accumsan et iusto odio dignissim qui blandi. Duis autem vel eum iriure dolor in hendrerit in vulputate velit esse molestie consequat, vel illum dolore eu feugiat nulla facilisis at vero eros et accumsan et iusto odio</p>
    </div>
    <a class="read-more" href="#">more &gt;&gt;</a>
  </section>
</main>

<footer class="site-footer">
  <svg class="to-top" width="40" height="40" viewBox="0 0 40 40"><circle cx="20" cy="20" r="18.5" fill="none" stroke="#fff" stroke-width="2.5"/><polyline points="10,24 20,14 30,24" fill="none" stroke="#fff" stroke-width="3.5"/></svg>
</footer>
</body>
</html>
```